Law Firm Website

I currently have a temporary site that I created myself at www.mcorveyfirm.net (hosted by 9tree). I am generally happy with the content.

My permanent website just has basic information right now: www.mcorveyfirm.com (hosted by lumenrack). I want to take the general content from the temporary website and have a more professional looking website on the permanent website. I want it in Wordpress format. I want a link to my blog: www.crookedpath.com. I want it to work on pads and smart phones. My number and e-mail address should be available on every page. The idea is to feature the potential client more than the lawyer.
Updates

Several of the designs are good. I would like the front page to have my number and address at the top (and at the top of every page) and to identify my law firm as "Law Office of Gerald T. Corvey". No need to include "mcorveyfirm" as that is just the web address. I like showing the most recent blog posts on the front page. I don't need video. No need to emphasize office hours or map location on the front page (that could be under a contact button). My picture should be somewhere. I would like an image from Boston on the front page if we can find one that is not copyright protected. No images of gavels or scales of justice. See some of the sample websites I listed in previous messages. Thanks!

Industry/Entity Type

Law Firm

```html
<!DOCTYPE html>
<html lang="en">
<head>
<meta charset="utf-8">
<title>Law Office of Gerald T. Corvey</title>
<link rel="stylesheet" href="https://fonts.googleapis.com/css2?family=Open+Sans:wght@400;600&family=Noto+Sans:wght@400;700&display=swap">
<style>
:root{
  --page-bg:#161616;
  --header-bg:#232323;
  --teal:#1f8aa8;
  --heading-blue:#1d6b94;
  --text:#222222;
  --sidebar-bg:#f1f1f1;
  --field-bg:#e6e6e6;
  --field-border:#d6d6d6;
  --footer-bg:#202020;
  --footer-line:#333333;
  --bottom-bg:#2a2a2a;
  --accent:#2aa6c8;
  --white:#ffffff;
}
*{margin:0;padding:0;box-sizing:border-box}
html,body{width:835px;height:1200px;overflow:hidden;background:var(--page-bg)}
body{position:relative;font-family:"Noto Sans",Arial,sans-serif;color:var(--text)}
.site{position:absolute;left:40px;top:34px;width:755px;height:1166px}
.header{position:absolute;left:0;top:0;width:755px;height:78px;background:var(--header-bg)}
.logo{position:absolute;left:0;top:0;width:141px;height:78px;background:linear-gradient(180deg,#2b9dbd,#1a7898);color:var(--white);font-family:"Open Sans",Arial,sans-serif;font-size:26px;line-height:30px;text-align:center;padding-top:8px;letter-spacing:-0.8px}
.header-address{position:absolute;right:12px;top:9px;color:#eee;font-size:10px;white-space:nowrap}
.header-phone{position:absolute;right:12px;top:24px;color:var(--white);font-family:"Open Sans",Arial,sans-serif;font-size:15.5px;white-space:nowrap}
.nav{position:absolute;left:152px;top:58px;width:592px;display:flex;justify-content:space-between;list-style:none}
.nav li{color:var(--white);font-size:9.4px;white-space:nowrap;line-height:14px}
.hero{position:absolute;left:0;top:78px;width:755px;height:139px}
.hero-bg{position:absolute;inset:0;background:linear-gradient(100deg,#1a8fae 0%,#136a8c 45%,#1a7fa0 60%,#0c4a68 100%)}
.hero-col{position:absolute;top:0;height:139px;padding:6px 0 0 18px;color:var(--white)}
.hero-col h2{font-family:"Open Sans",Arial,sans-serif;font-weight:400;font-size:23.5px;letter-spacing:-0.6px;line-height:32px}
.hero-col p{font-size:11px;line-height:15.4px;margin-top:4px;width:305px;color:#eef6fa}
.hero-divider{position:absolute;left:378px;top:0;width:1px;height:139px;background:rgba(255,255,255,0.35)}
.main{position:absolute;left:0;top:217px;width:755px;height:737px;background:var(--white)}
.content{position:absolute;left:18px;top:14px;width:495px}
.content h1,.content h2{font-family:"Open Sans",Arial,sans-serif;font-weight:400;color:var(--heading-blue);font-size:19px;letter-spacing:-0.4px}
.content p{font-size:11.2px;line-height:16px;margin-top:9px}
.specializations{margin-top:28px}
.spec-list{list-style:none;margin-top:8px}
.spec-list li{font-size:11.2px;line-height:19.8px;position:relative;padding-left:14px}
.spec-list li::before{content:"";position:absolute;left:1px;top:7px;width:6px;height:6px;border-radius:50%;background:#222}
.sidebar{position:absolute;left:535px;top:0;width:220px;height:401px;background:var(--sidebar-bg);padding:14px 14px 0 14px}
.sidebar h2{font-family:"Open Sans",Arial,sans-serif;font-weight:400;font-size:19px;letter-spacing:-0.5px;color:#111}
.sidebar p{font-size:11.4px;line-height:16px;margin-top:10px;width:180px}
.field{width:178px;height:31px;background:var(--field-bg);border:1px solid var(--field-border);font-size:11.2px;padding:7px 8px;margin-top:9px;color:#333}
.field:first-of-type{margin-top:14px}
.field.message{height:88px}
.send-button{display:inline-block;margin-top:11px;width:100px;height:31px;border-radius:4px;background:linear-gradient(180deg,#2a8fb6,#125b84);color:var(--white);font-size:11.6px;text-align:center;line-height:29px;border:1px solid #0e4a6b}
.footer{position:absolute;left:0;top:954px;width:755px;height:143px;background:var(--footer-bg)}
.footer-map{position:absolute;left:0;top:0;width:243px;height:143px;background:radial-gradient(circle at 50% 40%,#4a4a4a 0%,#2a2a2a 70%,#202020 100%)}
.footer-col{position:absolute;top:0;height:143px;padding:12px 20px 0 20px;color:#f2f2f2}
.footer-col h3{font-family:"Open Sans",Arial,sans-serif;font-weight:400;font-size:19px;letter-spacing:-0.5px}
.footer-col h3 span{color:var(--accent)}
.footer-col p{font-size:9.4px;line-height:16px;margin-top:9px}
.footer-divider{position:absolute;top:8px;width:1px;height:128px;background:var(--footer-line)}
.bottom-bar{position:absolute;left:0;top:1097px;width:755px;height:69px;background:var(--bottom-bg);padding:10px 24px;color:#7a7a7a}
.copyright{font-size:6.8px}
.disclaimer{font-size:6.8px;line-height:10px;margin-top:15px}
</style>
</head>
<body>
<div class="site">
  <header class="header">
    <div class="logo">Gerald<br>T. Corvey</div>
    <div class="header-address">48 Harlow St. 3rd Floor, Boston, MA 02110</div>
    <div class="header-phone">Call Today : 617 555-0142</div>
    <ul class="nav">
      <li>Home</li><li>Why Hire Me?</li><li>Success Stories</li><li>Practice Areas</li><li>Representative Clients</li><li>Services Provided</li><li>Contact Us</li><li>How To Find Us</li>
    </ul>
  </header>

  <section class="hero">
    <div class="hero-bg" role="img" aria-label="Blue-toned photograph of downtown Boston"></div>
    <div class="hero-col" style="left:0;width:378px">
      <h2>Why Hire Me?</h2>
      <p>I give real, practical advice to keep you out of trouble, stay in business and make money. I won't bore you with legal theories, but will explain how the legal issues affect your business.</p>
    </div>
    <div class="hero-divider"></div>
    <div class="hero-col" style="left:378px;width:377px">
      <h2>Expertise in Employment</h2>
      <p>I don't do everything. I don't handle personal injury claims, criminal matters, divorces, real estate transactions, bankruptcies, etc. (I can refer you to excellent lawyers who do these things).</p>
    </div>
  </section>

  <main class="main">
    <article class="content">
      <h1>Expertise in Employment and Business Law</h1>
      <p>I don't do everything. &nbsp;I don't handle personal injury claims, criminal matters, divorces, real estate transactions, bankruptcies, etc. (I can refer you to excellent lawyers who do these things). &nbsp;I would rather be great at a few things than okay, or worse, at everything. Employment and business law are very complicated. &nbsp;There are numerous state and federal statutes, regulations, guidelines, and countless court decisions. &nbsp;A lawyer cannot stay on top of it all by dabbling in the fields. &nbsp;You have to live it and breath it every day. &nbsp;See my blog at www.crookedpath.com to see my dedication to my limited fields.</p>
      <h2 class="specializations">Our Specializations</h2>
      <ul class="spec-list">
        <li>Employment Counseling and Litigation</li>
        <li>Hiring and Firing.</li>
        <li>Wage and Hour Issues.</li>
        <li>Noncompetes.</li>
        <li>Sexual Harassment.</li>
        <li>Leave Issues under the ADA, FMLA and State Law.</li>
        <li>Business Litigation</li>
        <li>Interference with Contractual Relations.</li>
        <li>Breach of Contract.</li>
        <li>Defamation (slander and lible).</li>
        <li>Unfair and Deceptive Business Practices under Chapter 93A.</li>
        <li>Litigation Avoidance</li>
        <li>Contract review and drafting.</li>
        <li>Employee handbooks.</li>
        <li>Non-Compete Agreements.</li>
        <li>Employee Hiring and Firing.</li>
        <li>Dealing with Rogue Employees.</li>
        <li>Businsess partner/shareholder Disputes.</li>
      </ul>
      <p>Whether you are a partner, minority or majority shareholder, or member of an LLC, you have rights if you business partners are treating you unfairly, stealing from the company, firing you, or acting in a way that requires termination. &nbsp;This area of law is tricky because business partners owe one another a duty of the utmost good faith and fair dealing. &nbsp;You need legal advice before you make a major decision. &nbsp;See my "Success Stories" for the results I have achieved for clients involved in these disputes.</p>
    </article>

    <aside class="sidebar">
      <h2>Contact Us Today</h2>
      <p>If you have questions or want to make an appointment then contact us:</p>
      <div class="field">Name</div>
      <div class="field">Email</div>
      <div class="field">Phone</div>
      <div class="field message">Message</div>
      <div class="send-button">Send us Email!</div>
    </aside>
  </main>

  <footer class="footer">
    <div class="footer-map" role="img" aria-label="Faint street map of the office neighborhood"></div>
    <div class="footer-col" style="left:0;width:243px">
      <h3>Contact <span>Info</span></h3>
      <p>Law Office of Gerald T. Corvey<br>48 Harlow St. 3rd Floor, Boston, MA 02110<br>Phone: 617 555-0142<br>Fax: 857 555-0198<br>Email: gcorvey@mcorveyfirm.com</p>
    </div>
    <div class="footer-divider" style="left:243px"></div>
    <div class="footer-col" style="left:243px;width:250px">
      <h3>Office <span>Hours</span></h3>
      <p>We can be reached during the following hours:<br>Monday Thru Friday 10am-6pm</p>
    </div>
    <div class="footer-divider" style="left:493px"></div>
    <div class="footer-col" style="left:493px;width:262px">
      <h3>Successes</h3>
      <p>A recent study shows that plaintiffs in most diversity cases never asked a judge to "certify a class" of those covered in the suit.</p>
    </div>
  </footer>

  <div class="bottom-bar">
    <div class="copyright">Copyright © 2014 Law office of Gerald T. Corvey. All Right Reserved</div>
    <div class="disclaimer">The information on this website is for general information purposes only. Nothing on this site should be taken as legal advice for any individual case or situation.<br>This information is not intended to create, and receipt or viewing does not constitute, an attorney-client relationship.</div>
  </div>
</div>
</body>
</html>
```